Law firm website marketed direct to many individual clients

I need someone to design a very basic website for a law firm that will be very eye catching. It's going to be a single-paged, scrolling website with a small number of folds. I have uploaded a simple word document that outlines the basics of what I thought could be the layout, but I am open to suggestion on font, size, shades of color, organization, etc. etc. Essentially the website just needs to be a very efficient and visually appealing way of conveying some simple messages.

Target Market(s)

High volumes of individuals who have gotten into a car accident and then google on their phones a lawyer to hire to represent them.

Industry/Entity Type

Legal

Number of Pages Required

1 page

Font styles to use
Serif
Sans Serif

Colors
34a7d7
85cae6
0592cd

Requirements
Must have
• Must be bright and grab the users attention with color scheme and layout. The different sections should be done in such a way that they can fit entirely onto one smart phone or tablet screen.
Nice to have
• I'd like to try and see what it looks like if in the middle somewhere there is a fold that says "MEET YOUR ATTORNEYS" and includes individual photos of two attorneys, one on the left side and one on the right. And then a small bio section on them. I don't want the photos to include a square or rectangle background, I want the person in the photo to be superimposed on top of whatever pattern or background you have in the fold.
Should not have
• Do not want too much text. Anything more than 2 sentences in any single place is unacceptable.

```html
<!DOCTYPE html>
<html lang="en">
<head>
<meta charset="utf-8">
<title>Harborline Legal</title>
<link href="https://fonts.googleapis.com/css2?family=Cinzel:wght@400;600;700&family=Arimo&display=swap" rel="stylesheet">
<style>
  :root{
    --blue-deep:#0592cd;
    --blue-mid:#34a7d7;
    --blue-light:#85cae6;
    --white:#ffffff;
    --ink:#555555;
  }
  *{margin:0;padding:0;box-sizing:border-box}
  html,body{width:1043px;height:1200px;overflow:hidden;background:var(--white)}
  body{position:relative;font-family:"Cinzel",serif;color:var(--white)}
  .band{position:absolute;left:0;width:1043px}
  .center{position:absolute;left:0;width:100%;text-align:center;transform:translateY(-50%);line-height:1.1}
  .site-header{top:0;height:56px;background:var(--white);border-top:3px solid var(--blue-light)}
  .brand{position:absolute;left:114px;top:28px;transform:translateY(-50%);font-size:20px;font-weight:600;color:var(--blue-deep);letter-spacing:.5px}
  .header-call{position:absolute;left:769px;top:14px;display:flex;align-items:center;gap:8px;color:var(--blue-deep)}
  .header-call .label{font-size:13px;font-weight:600;line-height:1}
  .header-call .num{font-size:19px;font-weight:700;line-height:1.1}
  .icon{width:26px;height:26px;flex:none}
  .hero{top:56px;height:241px;background:var(--blue-deep)}
  .hero-title{top:47px;font-size:38px;font-weight:600}
  .hero-sub{top:109px;font-size:26px;font-weight:600}
  .call-btn{position:absolute;left:400px;width:241px;height:47px;border:2px solid currentColor;border-radius:3px;display:flex;align-items:center;justify-content:center;gap:12px}
  .call-btn .word{font-size:14px;font-weight:600}
  .call-btn .num{font-size:20px;font-weight:700}
  .hero .call-btn{top:160px;color:var(--white)}
  .benefits{top:297px;height:458px;background:var(--white)}
  .benefit-title{font-size:30px;font-weight:600;color:var(--blue-mid)}
  .benefit-text{font-size:17px;font-weight:700;color:var(--ink)}
  .benefits .call-btn{top:366px;color:var(--blue-mid)}
  .promise{top:755px;height:302px;background:var(--blue-mid)}
  .promise-title{font-size:33px;font-weight:600}
  .promise-text{font-size:13px;font-weight:700;line-height:1.6}
  .promise .call-btn{top:216px;color:var(--white)}
  .site-footer{top:1057px;height:143px;background:var(--blue-deep);border-top:2px solid var(--blue-light)}
  .footer-name{font-size:13px;font-weight:700}
  .footer-addr{font-size:14px;font-weight:700}
  .footer-phone{display:flex;justify-content:center;align-items:center;gap:12px;font-size:20px;font-weight:700}
  .copyright{font-family:"Arimo",sans-serif;font-size:12px}
</style>
</head>
<body>
<svg width="0" height="0" style="position:absolute">
  <symbol id="phone" viewBox="0 0 32 32">
    <circle cx="16" cy="16" r="14.5" fill="none" stroke="currentColor" stroke-width="1.6"/>
    <path d="M13 8.5c-1.6.3-3 1.8-2.8 4 .4 4.3 3.2 9 7 11 1.6.8 3.4.3 4.2-1.1l.4-.8-3.2-2.2-1.3 1.2c-1.8-1-3.4-3.6-3.8-5.6l1.6-.8-.9-3.9z" fill="none" stroke="currentColor" stroke-width="1.5" stroke-linejoin="round"/>
  </symbol>
</svg>

<header class="band site-header">
  <div class="brand">Harborline Legal</div>
  <div class="header-call">
    <svg class="icon"><use href="#phone"/></svg>
    <div><div class="label">Call Us Today</div><div class="num">504-555-0148</div></div>
  </div>
</header>

<section class="band hero">
  <h1 class="center hero-title">Accident? Injured?</h1>
  <p class="center hero-sub">Your Case, Your Money</p>
  <div class="call-btn"><svg class="icon"><use href="#phone"/></svg><span class="word">Call</span><span class="num">504-555-0148</span></div>
</section>

<section class="band benefits">
  <h2 class="center benefit-title" style="top:52px">Low Fees</h2>
  <p class="center benefit-text" style="top:78px">We charge less, so you keep more.</p>
  <h2 class="center benefit-title" style="top:138px">Free Consultation</h2>
  <p class="center benefit-text" style="top:164px">It’s always free to talk to us.</p>
  <h2 class="center benefit-title" style="top:224px">Get Started Using Only Your Phone</h2>
  <p class="center benefit-text" style="top:249px">No need to come to the office, sign up using your phone.</p>
  <h2 class="center benefit-title" style="top:306px">Speak Directly To A Lawyer</h2>
  <p class="center benefit-text" style="top:331px">No staff screening. Talk right to a lawyer on your first call.</p>
  <div class="call-btn"><svg class="icon"><use href="#phone"/></svg><span class="word">Call</span><span class="num">504-555-0148</span></div>
</section>

<section class="band promise">
  <h2 class="center promise-title" style="top:52px">NO FEE UNLESS WE WIN</h2>
  <p class="center promise-text" style="top:75px">We don’t get paid unless you get paid. It’s as simple as that. We let our results do the talking for us.</p>
  <h2 class="center promise-title" style="top:132px">QUESTIONS ABOUT ANYTHING?</h2>
  <p class="center promise-text" style="top:171px">We’re here to help. Feel free to call us at 504-555-0148 to speak to one of our attorneys. With extensive<br>experience in helping clients get the results that they want, our team is always just a phone call away.</p>
  <div class="call-btn"><svg class="icon"><use href="#phone"/></svg><span class="word">Call</span><span class="num">504-555-0148</span></div>
</section>

<footer class="band site-footer">
  <p class="center footer-name" style="top:30px">Harborline Legal</p>
  <p class="center footer-addr" style="top:53px">Magnolia Street Office, New Orleans, LA 70112</p>
  <div class="center footer-phone" style="top:81px"><svg class="icon"><use href="#phone"/></svg><span>504-555-0148</span></div>
  <p class="center copyright" style="top:116px">Copyright © 2016 HarborlineLegal . All Rights Reserved.</p>
</footer>
</body>
</html>
```